Tarvel Plumbing Solutions

This is for my new plumbing company, I have attached an example of what I’m going for but want it to look better.

Target Market(s)

Home owners, real estate, etc.

Industry/Entity Type

Plumbing

Font styles to use
Other font styles liked:
• As per my logo and other examples uploaded

Colors

Designer to choose colors to be used in the design.

Requirements
Must have
• Must include my logo provided and similar to my flyer I have attached but better

```html
<!DOCTYPE html>
<html lang="en">
<head>
<meta charset="utf-8">
<title>Tarvel Plumbing Solutions – Flyer</title>
<link href="https://fonts.googleapis.com/css2?family=Montserrat:wght@500;600;700;800&family=Roboto:wght@400;500&display=swap" rel="stylesheet">
<style>
  :root {
    --navy: #1c3a5e;
    --blue: #2a93d8;
    --blue-light: #4fb0ea;
    --orange: #f26a1b;
    --tile: #f0f1f3;
    --ink: #1d2733;
    --paper: #ffffff;
    --backdrop: #e6e8eb;
  }
  * { box-sizing: border-box; margin: 0; padding: 0; }
  html, body { width: 1200px; height: 1200px; overflow: hidden; }
  body {
    background: var(--backdrop);
    font-family: "Roboto", Arial, sans-serif;
    color: var(--ink);
    position: relative;
  }
  .flyer {
    position: absolute; left: 280px; top: 102px;
    width: 640px; height: 996px;
    background: var(--paper);
    overflow: hidden;
    box-shadow: 0 10px 30px rgba(0,0,0,.15);
  }
  .brand {
    position: absolute; top: 44px; left: 0; width: 100%;
    display: flex; flex-direction: column; align-items: center;
  }
  .brand-name {
    display: flex; align-items: center; gap: 10px;
    font-family: "Montserrat", sans-serif; font-weight: 800;
    font-size: 40px; color: var(--navy); letter-spacing: .5px; line-height: 1;
  }
  .brand-dot { width: 16px; height: 16px; border-radius: 50%; background: var(--orange); }
  .brand-tag {
    margin-top: 8px;
    font-family: "Montserrat", sans-serif; font-weight: 600;
    font-size: 12px; color: var(--navy); letter-spacing: .4px;
  }
  .hero { position: absolute; top: 128px; left: 0; width: 640px; height: 300px; }
  .hero-photo { position: absolute; top: 16px; height: 212px; }
  .hero-photo--splash { left: 0; width: 330px; background: radial-gradient(ellipse at 45% 60%, #6fc4f2 0%, #2a8fd6 45%, #0f4f8a 100%); }
  .hero-photo--tap { left: 330px; width: 310px; background: linear-gradient(160deg, #6b4e34 0%, #2b2a2c 45%, #1a2530 100%); }
  .hero-shapes { position: absolute; inset: 0; }
  .headline {
    position: absolute; top: 247px; left: 0; width: 100%;
    text-align: center; color: #fff;
    font-family: "Montserrat", sans-serif; font-weight: 600;
    font-size: 27px; letter-spacing: .2px;
  }
  .section-title {
    position: absolute; top: 440px; left: 0; width: 100%;
    text-align: center;
    font-family: "Montserrat", sans-serif; font-weight: 700; font-size: 27px;
  }
  .services {
    position: absolute; top: 494px; left: 30px; width: 580px;
    display: grid; grid-template-columns: repeat(4, 1fr); gap: 12px 11px;
  }
  .service {
    height: 124px; background: var(--tile); border-radius: 6px;
    display: flex; flex-direction: column; align-items: center; justify-content: center;
    text-align: center; padding: 0 4px;
  }
  .service svg { width: 34px; height: 34px; margin-bottom: 10px; stroke: var(--navy); fill: none; stroke-width: 1.6; stroke-linecap: round; stroke-linejoin: round; }
  .service-name { font-size: 13px; line-height: 1.3; color: var(--ink); }
  .promo {
    position: absolute; top: 798px; left: 36px;
    font-family: "Roboto", sans-serif; font-size: 21px; line-height: 1.28; color: var(--ink);
  }
  .promo strong { font-weight: 500; }
  .promo-rule { position: absolute; top: 852px; left: 36px; width: 110px; height: 6px; background: var(--blue); }
  .promo-rule::after { content: ""; position: absolute; right: -28px; top: 0; width: 22px; height: 6px; background: var(--orange); }
  .badge {
    position: absolute; left: 494px; top: 770px; width: 110px; height: 110px;
    border-radius: 50%; background: var(--orange);
    border: 4px solid #fff; outline: 3px solid var(--orange);
    display: flex; align-items: center; justify-content: center; text-align: center;
    color: #fff; font-family: "Montserrat", sans-serif; font-weight: 700;
    font-size: 12px; line-height: 1.25;
  }
  .footer { position: absolute; left: 0; top: 876px; width: 640px; height: 120px; }
  .footer svg { position: absolute; inset: 0; }
  .contact {
    position: absolute; color: #fff; font-size: 14px;
    display: flex; align-items: center; gap: 8px;
  }
  .contact svg { position: static; width: 15px; height: 15px; }
  .contact--phone { left: 36px; top: 48px; }
  .contact--email { left: 36px; top: 72px; }
  .contact--handle { right: 36px; top: 72px; }
  .socials { position: absolute; right: 36px; top: 48px; display: flex; gap: 7px; }
  .socials span { width: 14px; height: 14px; border-radius: 50%; background: #fff; }
</style>
</head>
<body>
<main class="flyer">
  <header class="brand">
    <div class="brand-name"><span class="brand-dot"></span>Tarvel</div>
    <div class="brand-tag">PLUMBING SOLUTIONS</div>
  </header>

  <section class="hero">
    <div class="hero-photo hero-photo--splash" role="img" aria-label="Photo of a water droplet splashing into clear blue water"></div>
    <div class="hero-photo hero-photo--tap" role="img" aria-label="Photo of a running kitchen tap over a sink"></div>
    <svg class="hero-shapes" viewBox="0 0 640 300" aria-hidden="true">
      <polygon points="0,0 130,0 150,20 0,20" fill="#f26a1b"/>
      <polygon points="0,20 150,20 135,38 0,38" fill="#2a93d8" opacity=".9"/>
      <polygon points="520,0 640,0 640,20 505,20" fill="#f26a1b"/>
      <polygon points="0,196 80,196 70,216 0,216" fill="#2a93d8"/>
      <polygon points="560,196 640,196 640,212 548,212" fill="#f26a1b"/>
      <polygon points="320,50 362,122 320,194 278,122" fill="#2a93d8" stroke="#ffffff" stroke-width="5"/>
      <rect x="0" y="212" width="640" height="80" fill="#1c3a5e"/>
      <polygon points="190,292 460,292 475,310 175,310" fill="#2a93d8"/>
      <polygon points="0,292 190,292 175,310 0,310" fill="#f26a1b"/>
      <polygon points="460,292 640,292 640,300 468,300" fill="#f26a1b"/>
    </svg>
    <h1 class="headline">RELIABLE PLUMBING. REAL SOLUTIONS.</h1>
  </section>

  <h2 class="section-title">Our Services</h2>

  <section class="services">
    <div class="service"><svg viewBox="0 0 34 34"><path d="M6 14h14v6H6zM13 14V9M9 9h8M20 16h5a3 3 0 0 1 3 3v3"/><path d="M28 25v3"/></svg><div class="service-name">Emergency Plumbing</div></div>
    <div class="service"><svg viewBox="0 0 34 34"><path d="M5 8h18v6H5zM14 14v8h10v6h6v-12H20"/></svg><div class="service-name">Drainage Maintenance</div></div>
    <div class="service"><svg viewBox="0 0 34 34"><path d="M8 6h8v8M16 10h6v8"/><path d="M19 22c0 3 2 5 3 5s3-2 3-5c0-2-3-5-3-5s-3 3-3 5z"/></svg><div class="service-name">Gas Maintenance</div></div>
    <div class="service"><svg viewBox="0 0 34 34"><path d="M6 24l12-12 4 4-12 12zM18 12l4-6 8 4-4 6"/></svg><div class="service-name">Gas Maintenance</div></div>
    <div class="service"><svg viewBox="0 0 34 34"><path d="M15 6c0 0-8 9-8 15a8 8 0 0 0 16 0c0-6-8-15-8-15z"/><circle cx="25" cy="12" r="3"/></svg><div class="service-name">Hot Water<br>Systems</div></div>
    <div class="service"><svg viewBox="0 0 34 34"><path d="M6 6h14v8H6zM20 10h6v8M10 14v14h12V20"/></svg><div class="service-name">Leaking<br>Fixtures</div></div>
    <div class="service"><svg viewBox="0 0 34 34"><rect x="5" y="8" width="12" height="20" rx="2"/><rect x="20" y="14" width="9" height="14" rx="2"/><circle cx="25" cy="8" r="3"/></svg><div class="service-name">Blocked Sewer &amp;<br>Stormwater</div></div>
    <div class="service"><svg viewBox="0 0 34 34"><circle cx="17" cy="15" r="7"/><circle cx="17" cy="15" r="3"/><path d="M6 28h22M9 28v-4h16v4M17 5v3"/></svg><div class="service-name">Camera &amp;<br>TMV Maintenance</div></div>
  </section>

  <p class="promo">MENTION THIS FLYER TO RECEIVE<br><strong>15% OFF YOUR FIRST SERVICE</strong></p>
  <div class="promo-rule"></div>
  <div class="badge">DISCOUNT<br>OFFER<br>HIGHLIGHT</div>

  <footer class="footer">
    <svg viewBox="0 0 640 120" aria-hidden="true">
      <polygon points="0,18 120,18 138,34 0,34" fill="#f26a1b"/>
      <polygon points="470,4 640,4 640,18 486,18" fill="#f26a1b"/>
      <polygon points="0,30 140,30 160,18 640,18 640,120 0,120" fill="#2a93d8"/>
    </svg>
    <div class="contact contact--phone"><svg viewBox="0 0 16 16"><path d="M4 1l3 3-2 2c1 2 3 4 5 5l2-2 3 3-2 3C7 15 1 9 1 3z" fill="#fff"/></svg>0400 555 219</div>
    <div class="contact contact--email"><svg viewBox="0 0 16 16"><rect x="1" y="3" width="14" height="10" rx="1" fill="#fff"/><path d="M1 4l7 5 7-5" stroke="#2a93d8" stroke-width="1.4" fill="none"/></svg>hello@tarvelplumbing.net</div>
    <div class="socials"><span></span><span></span><span></span><span></span></div>
    <div class="contact contact--handle"><svg viewBox="0 0 16 16"><circle cx="8" cy="8" r="7" fill="#fff"/></svg>@TarvelPlumbingSolutions</div>
  </footer>
</main>
</body>
</html>
```